New design for our thank you cards *

We need Thank You card designs for our mortgage broking company "Copperleaf Lending". We have an existing design and need a revamp of these. We are a boutique broking firm and would like "thank you" cards to send to our clients who refer new clients.

We are a referral-based business, our success and longevity is inextricably linked to the advice and service we provide our clients and referral partners.

Industry/Entity Type

Mortgage Brokerage

Colors
0792cd
0255a3
3176b5
33a6d7
85acd3
85cae6
cee9f5
cedeed
ffffff

Requirements
Must have
• our logo on the front 7 thank you & print on the back

```html
<!DOCTYPE html>
<html lang="en">
<head>
<meta charset="UTF-8">
<title>Copperleaf Lending – Thank You Card</title>
<link rel="stylesheet" href="https://fonts.googleapis.com/css2?family=Dosis:wght@400;600&display=swap">
<style>
  :root {
    --stage: #b2b2b2;
    --card: #fafafa;
    --ink: #111111;
    --sky-pale: #cee9f5;
    --sky-soft: #85cae6;
    --navy: #2b3790;
    --brand-ink: #333333;
  }
  * { margin: 0; padding: 0; box-sizing: border-box; }
  html, body {
    width: 1200px;
    height: 515px;
    overflow: hidden;
    background: var(--stage);
  }
  .canvas {
    position: relative;
    width: 1200px;
    height: 515px;
    background: var(--stage);
  }
  .card {
    position: absolute;
    top: 145px;
    width: 372px;
    height: 224px;
    background: var(--card);
  }
  .card--front { left: 216px; }
  .card--back { left: 611px; }

  .perched-birds {
    position: absolute;
    left: 16px;
    top: 52px;
    width: 296px;
    height: 38px;
    background: linear-gradient(90deg, var(--sky-soft) 0%, var(--sky-pale) 50%, var(--sky-soft) 100%);
  }

  .thank-you {
    position: absolute;
    left: 0;
    right: 0;
    top: 82px;
    text-align: center;
    font-family: "Dosis", sans-serif;
    font-weight: 400;
    font-size: 82px;
    line-height: 1;
    letter-spacing: -1px;
    color: var(--ink);
    transform: scaleX(0.86);
  }

  .brand {
    position: absolute;
    left: 0;
    right: 0;
    top: 131px;
    display: flex;
    flex-direction: column;
    align-items: center;
  }
  .brand__square {
    width: 30px;
    height: 30px;
    background: var(--navy);
    margin-bottom: 6px;
  }
  .brand__name {
    font-family: "Dosis", sans-serif;
    font-weight: 600;
    font-size: 10px;
    line-height: 11px;
    letter-spacing: 1px;
    text-transform: uppercase;
    text-align: center;
    color: var(--brand-ink);
  }
</style>
</head>
<body>
  <main class="canvas">
    <section class="card card--front">
      <div class="perched-birds" role="img" aria-label="Two blue birds with small leaves perched on the Thank You lettering"></div>
      <h1 class="thank-you">THANK YOU</h1>
    </section>
    <section class="card card--back">
      <div class="brand">
        <span class="brand__square"></span>
        <span class="brand__name">Copperleaf<br>Lending</span>
      </div>
    </section>
  </main>
</body>
</html>
```